Women's Empowerment & Prayer Brunch - Matching Poster, flyer and Postcard

We are a Christian Event & Travel Company and we are hosting our inaugural event on June 10, 2017. This event is a women's empowerment & prayer brunch aboard a private yacht leaving out of Larkspur Landing, Maryland. The event will cater to women who have a vision to start or have already embarked on the journey of starting or growing a business or ministry. The event calls for a matching poster, flyer and postcard design that give an elegant & exquisite feel with just the right breath of freshness. The colors should reflect our logo as this is our launch event. I have also included 2 photos of the Coralwind Heritage Village production (one of our sponsors) - Please include but do not make it take over the design - this is to advertise the door prize. The final design will portray the branding of the company (Christian, travel, events, elegance, professional), the branding of the event (elegant and luxurious) and the importance of this launch event.
Please include the following information:
Brightwell Event & Travel Group presents
Event name: Climbing the Hill: Trust, Service & Devotion.
Tag Line/Description: An Exquisite Women's Empowerment & Prayer Brunch.
Guest Speaker: Minister Harriet L. Dunmore (Photo included)
VP of TrustLine
Asst. Pastor & First Lady of Gilead Baptist Church
Special Guest Psalmist: Minister Tessa Holbrook (Photo Included)
Worship Director of Stonefield Community Church
Vocalist, Songwriter, Musician, and Clinician
Venue: Aboard the Regal Tide Yacht
Dock: Larkspur Landing
342 Marlow Court, Oxen Hill, MD 20712
Boarding 10:00am
Sailing Promptly at 10:30am
(Please be on time the yacht will not wait)
Date: Saturday June 10, 2017
Tickets: Early Bird US$75.00/person (ends May 15, 2017)
Regular Tickets US$95.99
Purchase Tickets at www.brightwellevent-travel.example/climbing-the-hill
SPACE IS LIMITED DUE TO YACHT CAPACITY
Grand Prize: Julian Ardent Purse
Door Prize: 2 Tickets to the Islander Coralwind Heritage Village
Other prizes for special ladies in attendance.
Ladies are asked to dress in Elegant White Ensemble
Corporate Sponsors:
The Coralwind Heritage Village (Logo included)
R. Lanning Photography (Logo included)
Special Thanks to our Individual Sponsors:
Mrs. G. Whitlow, Mr. K Prentice & Mr. S. Dorsey

Target Market(s)

Women, Business, Ministry, Christians, Middle to Upper Class

Industry/Entity Type

Events

Font styles to use
Serif
Script

Requirements
Must have
• Elegance, professional, vivid in color & font. be creative in Visual and FONT!
• Poster: 18" X 24"
• Flyer: one sided.
• ***** the final design chosen will have a cross referenced design of 1 flyer, 1 postcard 1 poster. This was included so you have a reference - Be creative!!!!!!
Nice to have
• Matching across all 3 designs (poster, flyer & postcard) but sized appropriately and just enough difference to play up the design and be appealing.
• I uploaded 3 example flyers to give you inspiration of the type of visuals I'm looking for. I removed my amateur sample because the designs were copying it instead of being creative.
Should not have
• Any thing inappropriate, alcohol oriented or sexual

```html
<!DOCTYPE html>
<html lang="en">
<head>
<meta charset="utf-8">
<title>Climbing the Hill – Women's Empowerment &amp; Prayer Brunch</title>
<link rel="stylesheet" href="https://fonts.googleapis.com/css2?family=Pinyon+Script&family=Libre+Bodoni:ital,wght@1,700&family=Michroma&family=Arimo:wght@400;700&display=swap">
<style>
:root{
  --night-top:#0c1530;
  --night-mid:#1b2a58;
  --night-low:#2a3a70;
  --water-light:#c9ccd8;
  --water-mid:#5c6597;
  --water-deep:#1e2566;
  --gold:#e2b93b;
  --gold-deep:#b88a1c;
  --white:#ffffff;
  --soft:#e6e8f2;
  --navy-text:#1d2150;
}
*{margin:0;padding:0;box-sizing:border-box}
html,body{width:900px;height:1200px;overflow:hidden;background:var(--night-top)}
.poster{position:relative;width:900px;height:1200px;overflow:hidden;
  background:linear-gradient(180deg,var(--night-top) 0%,var(--night-mid) 45%,var(--night-low) 68.5%,var(--water-light) 69%,var(--water-mid) 80%,var(--water-deep) 100%);
  font-family:'Arimo',sans-serif;color:var(--white)}
.sky-glow{position:absolute;left:-60px;top:-30px;width:260px;height:260px;border-radius:50%;
  background:radial-gradient(circle,rgba(255,225,200,.55) 0%,rgba(200,150,120,.25) 30%,rgba(0,0,0,0) 70%)}
.water-sheen{position:absolute;left:0;top:822px;width:900px;height:378px;
  background:repeating-linear-gradient(180deg,rgba(255,255,255,.12) 0 3px,rgba(0,0,0,0) 3px 14px)}
.abs{position:absolute}
.center{left:0;width:900px;text-align:center}
.brand{top:50px;display:flex;justify-content:center;align-items:center;gap:10px}
.brand-dot{width:22px;height:22px;border:2px solid var(--gold);border-radius:50%}
.brand-name{font-family:'Libre Bodoni',serif;font-style:italic;font-weight:700;font-size:20px;color:var(--gold)}
.presents{top:136px;font-family:'Libre Bodoni',serif;font-size:12px;color:var(--soft)}
.title{top:140px;font-family:'Pinyon Script',cursive;font-size:82px;line-height:100px;
  text-shadow:0 2px 6px rgba(0,0,0,.6)}
.rule{left:0;width:900px;height:2px;background:var(--soft)}
.theme{top:267px;font-family:'Michroma',sans-serif;font-size:21px;letter-spacing:6px;color:var(--gold)}
.tagline{top:318px;font-family:'Michroma',sans-serif;font-size:12px;letter-spacing:3px;color:var(--soft)}
.date{top:347px;font-family:'Michroma',sans-serif;font-size:11px;letter-spacing:3px;color:var(--gold)}
.divider{left:452px;top:381px;width:2px;height:164px;background:var(--soft)}
.col-left{right:463px;text-align:right}
.col-right{left:469px}
.label{font-family:'Libre Bodoni',serif;font-style:italic;font-weight:700;font-size:14px;line-height:16px}
.info{font-size:13px;line-height:16px}
.bold{font-weight:700}
.photo{top:592px;width:122px;height:155px;border:3px solid var(--gold)}
.photo-speaker{left:315px;background:linear-gradient(160deg,#7a4a3a,#c2272d 60%,#5a1a1a)}
.photo-guest{left:469px;background:linear-gradient(160deg,#1a1a1a,#5a3a30 55%,#e8e4dc)}
.bio{font-size:10px;line-height:13px}
.bio-name{font-weight:700;font-size:10.5px}
.dress{top:781px;font-family:'Libre Bodoni',serif;font-style:italic;font-weight:700;font-size:15px;letter-spacing:1px}
.band{height:26px;background:linear-gradient(90deg,rgba(255,255,255,0),rgba(255,255,255,.75) 15%,rgba(255,255,255,.75) 85%,rgba(255,255,255,0))}
.seal{width:58px;height:58px;border-radius:50%;background:radial-gradient(circle at 40% 35%,#f3d572,var(--gold-deep));
  border:2px solid var(--navy-text);display:flex;align-items:center;justify-content:center;text-align:center;
  font-family:'Libre Bodoni',serif;font-style:italic;font-weight:700;font-size:11px;line-height:12px;color:var(--white);transform:rotate(-12deg)}
.prize{font-family:'Libre Bodoni',serif;font-style:italic;font-weight:700;color:var(--navy-text);letter-spacing:1.5px}
.sponsor-box{left:168px;top:1009px;width:560px;height:88px;background:var(--white)}
.sponsor-title{left:26px;top:12px;font-family:'Libre Bodoni',serif;font-style:italic;font-weight:700;font-size:24px;line-height:36px;color:var(--navy-text);letter-spacing:1px}
.sponsor-chip{left:188px;top:7px;width:101px;height:74px;background:#ececec;display:flex;align-items:center;justify-content:center;text-align:center;
  font-family:'Arimo',sans-serif;font-size:10px;color:#555;padding:4px}
.sponsor-name{left:324px;top:20px;width:220px;font-family:'Arimo',sans-serif;font-weight:700;font-size:20px;line-height:24px;color:var(--gold-deep);text-align:center}
.thanks{top:1113px;font-family:'Libre Bodoni',serif;font-style:italic;font-weight:700;font-size:11px;letter-spacing:1px}
.patrons{top:1137px;font-size:16px;letter-spacing:1px;color:var(--soft)}
</style>
</head>
<body>
<main class="poster">
  <div class="sky-glow"></div>
  <div class="water-sheen"></div>

  <header>
    <div class="abs center brand"><span class="brand-dot"></span><span class="brand-name">Brightwell Event &amp; Travel Group</span></div>
    <p class="abs center presents">presents</p>
    <h1 class="abs center title">Climbing the Hill</h1>
    <div class="abs rule" style="top:258px"></div>
    <p class="abs center theme">TRUST, SERVICE &amp; DEVOTION</p>
    <div class="abs rule" style="top:301px"></div>
    <p class="abs center tagline">An Exquisite Women's Empowerment &amp; Prayer Brunch</p>
    <p class="abs center date">SATURDAY JUNE 10, 2017</p>
  </header>

  <section class="details">
    <div class="abs divider"></div>
    <div class="abs col-left" style="top:390px">
      <p class="label">Dock:</p>
      <p class="info">Larkspur Landing</p>
      <p class="info">342 Marlow Court, Oxen Hill, MD 20712</p>
      <p class="label" style="margin-top:7px">Boarding:</p>
      <p class="info">10:00am</p>
      <p class="label" style="margin-top:7px">Sailing Promptly at:</p>
      <p class="info">10:30am</p>
      <p class="info bold">(Please be on time the yacht will not wait)</p>
    </div>
    <div class="abs col-right" style="top:406px">
      <p class="label">Tickets:</p>
      <p class="info">Early Bird US$75.00/person (ends May 15, 2017)</p>
      <p class="info">Regular Tickets US$95.99</p>
      <p class="label" style="margin-top:7px">Purchase Tickets at:</p>
      <p class="info" style="font-size:12px">www.brightwellevent-travel.example/climbing-the-hill</p>
      <p class="info bold" style="margin-top:7px;letter-spacing:.5px">SPACE IS LIMITED DUE TO YACHT CAPACITY</p>
    </div>
  </section>

  <section class="guests">
    <p class="abs col-left label" style="top:564px">Guest Speaker</p>
    <p class="abs col-right label" style="top:564px">Special Guest</p>
    <div class="abs photo photo-speaker" role="img" aria-label="Portrait of Minister Harriet L. Dunmore"></div>
    <div class="abs photo photo-guest" role="img" aria-label="Portrait of Minister Tessa Holbrook"></div>
    <div class="abs bio" style="right:602px;top:668px;text-align:right">
      <p class="bio-name">Minister Harriet L. Dunmore</p>
      <p style="margin-top:10px">VP of TrustLine</p>
      <p style="margin-top:10px">Asst. Pastor &amp; First Lady of</p>
      <p>Gilead Baptist Church</p>
    </div>
    <div class="abs bio" style="left:610px;top:668px">
      <p class="bio-name">Minister Tessa Holbrook</p>
      <p style="margin-top:10px">Worship Director of</p>
      <p>Stonefield Community Church</p>
      <p style="margin-top:10px">Vocalist, Songwriter, Musician, and Clinician</p>
    </div>
    <p class="abs center dress">Ladies are asked to dress in Elegant White Ensemble</p>
  </section>

  <section class="prizes">
    <div class="abs band" style="left:280px;top:854px;width:420px"></div>
    <div class="abs seal" style="left:295px;top:838px">GRAND<br>PRIZE</div>
    <p class="abs prize" style="left:376px;top:853px;font-size:23px">Julian Ardent Purse</p>
    <div class="abs band" style="left:0;top:911px;width:700px"></div>
    <p class="abs prize" style="left:70px;top:913px;font-size:16px">2 Tickets to the Islander Coralwind Heritage Village</p>
    <div class="abs seal" style="left:650px;top:895px">DOOR<br>PRIZE</div>
    <div class="abs" style="left:168px;top:963px;width:560px;height:20px;background:rgba(255,255,255,.8)"></div>
    <p class="abs center prize" style="top:964px;font-size:13px">Other prizes for special ladies in attendance.</p>
  </section>

  <section class="abs sponsor-box">
    <p class="abs sponsor-title">Corporate<br>Sponsors</p>
    <div class="abs sponsor-chip">R. Lanning Photography</div>
    <p class="abs sponsor-name">Coralwind Heritage Village</p>
  </section>

  <footer>
    <p class="abs center thanks">Special Thanks to our Individual Sponsors:</p>
    <p class="abs center patrons">Mrs. G. Whitlow, Mr. K Prentice &amp; Mr. S. Dorsey</p>
  </footer>
</main>
</body>
</html>
```